Advertisement flyer (editable) and market report template in same style

Advertisement flyer (aka 1 page Media Kit) for us to sell advertising space on our website banner, tidecargomarket.com, and a market report template in the same style.
We would like to use colors that are used on our website. The flyer and market report template should be simple, and professional-looking. It should not look "old" or "boring". I've attached two drafts (1 each respectively), and our logo.

Target Market(s)

30-60 year old men but should look cool, new-aged, and fresh.

Industry/Entity Type

Shipping

Font styles to use
Serif

Requirements
Must have
• Editable layout so we can adjust text, numbers, and graphics on all. A fresh and new look. Colors per www.TideCargoMarket.com website.
Should not have
• Boring layout and font

```html
<!DOCTYPE html>
<html lang="en">
<head>
<meta charset="utf-8">
<title>Tide Cargo Market – Media Kit</title>
<link href="https://fonts.googleapis.com/css2?family=Montserrat:wght@600;700;800&family=Open+Sans:wght@400;600;700&display=swap" rel="stylesheet">
<style>
  :root{
    --page:#e6e9ed;
    --blue:#1b6fc4;
    --blue-deep:#0b3f9c;
    --card:#0d47a6;
    --cyan:#19a6ea;
    --yellow:#f7b81b;
    --white:#ffffff;
    --ink:#2a2f36;
    --brand:#0d4fb0;
  }
  *{box-sizing:border-box;margin:0;padding:0}
  html,body{width:960px;height:1200px;overflow:hidden;background:var(--page)}
  body{font-family:"Open Sans",Arial,sans-serif}
  .flyer{position:absolute;left:40px;top:30px;width:880px;height:1140px;overflow:hidden;
    background:linear-gradient(180deg,#1766bd 0%,#1d78cc 30%,#2a8dd8 45%);box-shadow:0 6px 18px rgba(0,0,0,.18)}
  .hero-photo{position:absolute;left:0;top:470px;width:880px;height:358px;
    background:
      linear-gradient(180deg,rgba(42,141,216,1) 0%,rgba(120,185,228,.0) 30%),
      linear-gradient(160deg,#8cc3e6 0%,#2f8fc4 30%,#1f77ad 48%,#6f9aa6 62%,#a9755a 78%,#8e4a36 100%)}
  .logo-tab{position:absolute;left:0;top:0}
  .logo-tab .name{position:absolute;left:34px;top:38px;font-family:"Open Sans",Arial,sans-serif;font-weight:700;font-size:22px;color:var(--brand)}
  .title{position:absolute;right:50px;top:34px;text-align:right;color:var(--white)}
  .title .eyebrow{font-family:"Montserrat",sans-serif;font-weight:600;font-size:16px;letter-spacing:.3px}
  .title h1{font-family:"Montserrat",sans-serif;font-weight:800;font-size:46px;line-height:1.05;letter-spacing:1px}
  .tagline{position:absolute;left:0;width:880px;top:160px;text-align:center;color:var(--white);font-size:18px;line-height:25px}
  .divider{position:absolute;left:140px;width:600px;top:217px;height:2px;background:rgba(255,255,255,.6)}
  .claim{position:absolute;left:0;width:880px;top:232px;text-align:center;color:var(--white);
    font-family:"Montserrat",sans-serif;font-weight:700;font-size:19px;line-height:27px}
  .claim em{font-style:normal;color:var(--yellow)}
  .stat{position:absolute;top:384px;width:164px;height:213px;background:var(--card);color:var(--white);text-align:center;padding-top:68px}
  .stat .badge{position:absolute;left:22px;top:-60px}
  .stat .figure{font-family:"Montserrat",sans-serif;font-weight:800;font-size:40px;line-height:44px}
  .stat .label{font-family:"Montserrat",sans-serif;font-weight:700;font-size:20px;line-height:24px}
  .stat .label.sm{font-size:17px;line-height:21px}
  .stat .note{font-size:20px;line-height:26px}
  .stat .fine{font-size:14.5px;line-height:20px;padding:0 8px}
  .stat .fine b{font-weight:700}
  .cta{position:absolute;left:0;top:828px;width:880px;height:80px;background:var(--cyan);color:var(--white);text-align:center;padding-top:10px}
  .cta p{font-size:22px;line-height:30px}
  .cta a{font-weight:700;font-size:21px;color:var(--white);text-decoration:none}
  .footer{position:absolute;left:0;top:908px;width:880px;height:232px;background:var(--white)}
  .contact{position:absolute;left:58px;top:26px;color:var(--ink);font-size:18.5px;line-height:29px}
  .contact .org{font-family:"Montserrat",sans-serif;font-weight:700;color:var(--brand);font-size:19px;margin-bottom:6px}
  .contact .row{display:flex;align-items:flex-start;gap:10px}
  .contact .row svg{margin-top:7px;flex:none}
  .contact .gap{margin-top:8px}
  .footer-brand{position:absolute;right:50px;top:100px;font-family:"Open Sans",Arial,sans-serif;font-weight:700;font-size:30px;color:var(--brand)}
</style>
</head>
<body>
<main class="flyer">
  <div class="hero-photo" role="img" aria-label="Aerial photograph of a coastal port with turquoise sea, a ship and red ore stockyards"></div>

  <div class="logo-tab">
    <svg width="290" height="112" viewBox="0 0 290 112"><polygon points="0,0 285,0 240,110 0,110" fill="#fff"/></svg>
    <span class="name">TideCargoMarket</span>
  </div>

  <header class="title">
    <div class="eyebrow">TIDE CARGO MARKET</div>
    <h1>MEDIA KIT</h1>
  </header>

  <p class="tagline">We are the efficient online marketplace<br>for charterers and ship owners in the dry bulk, tanker, and gas markets.</p>
  <div class="divider"></div>
  <p class="claim">OUR USERS INCLUDE <em>OVER 75</em> MAJOR TRADING COMPANIES AND<br>SHIP OWNERS REPRESENTING <em>THOUSANDS OF VESSELS.</em></p>

  <section class="stat" style="left:62px">
    <svg class="badge" width="120" height="120" viewBox="0 0 120 120"><circle cx="60" cy="60" r="60" fill="#0d47a6"/><circle cx="60" cy="60" r="49" fill="none" stroke="#fff" stroke-width="3"/>
      <g fill="none" stroke="#fff" stroke-width="3"><rect x="40" y="36" width="30" height="40" rx="2"/><line x1="46" y1="46" x2="62" y2="46"/><line x1="46" y1="54" x2="58" y2="54"/><line x1="46" y1="62" x2="54" y2="62"/><circle cx="70" cy="68" r="9"/><line x1="76" y1="75" x2="84" y2="83"/></g></svg>
    <div class="figure">10K</div>
    <div class="label">PAGE VIEWS</div>
    <div class="note">in the last<br>30 days.</div>
  </section>

  <section class="stat" style="left:259px">
    <svg class="badge" width="120" height="120" viewBox="0 0 120 120"><circle cx="60" cy="60" r="60" fill="#0d47a6"/><circle cx="60" cy="60" r="49" fill="none" stroke="#fff" stroke-width="3"/>
      <g stroke="#fff" stroke-width="2.5" fill="none"><line x1="42" y1="44" x2="60" y2="36"/><line x1="60" y1="36" x2="78" y2="46"/><line x1="42" y1="44" x2="60" y2="58"/><line x1="78" y1="46" x2="60" y2="58"/><line x1="60" y1="36" x2="60" y2="58"/><line x1="42" y1="44" x2="40" y2="64"/><line x1="78" y1="46" x2="80" y2="64"/></g>
      <g fill="#fff"><circle cx="42" cy="44" r="4"/><circle cx="60" cy="36" r="4"/><circle cx="78" cy="46" r="4"/><circle cx="40" cy="64" r="4"/><circle cx="80" cy="64" r="4"/><circle cx="60" cy="62" r="6"/><path d="M48 84a12 12 0 0 1 24 0z"/></g></svg>
    <div class="figure">300+</div>
    <div class="label sm">REGISTERED<br>USERS</div>
  </section>

  <section class="stat" style="left:456px">
    <svg class="badge" width="120" height="120" viewBox="0 0 120 120"><circle cx="60" cy="60" r="60" fill="#0d47a6"/><circle cx="60" cy="60" r="49" fill="none" stroke="#fff" stroke-width="3"/>
      <g fill="#fff"><circle cx="60" cy="46" r="7"/><path d="M48 70a12 12 0 0 1 24 0z"/><circle cx="42" cy="54" r="5.5"/><path d="M33 74a9 9 0 0 1 18 0z"/><circle cx="78" cy="54" r="5.5"/><path d="M69 74a9 9 0 0 1 18 0z"/></g>
      <path d="M46 40a18 18 0 0 1 28 0" fill="none" stroke="#fff" stroke-width="2.5"/></svg>
    <div class="figure">100%</div>
    <div class="label sm">OF USERS</div>
    <div class="fine">are revenue generators and have purchasing power.</div>
  </section>

  <section class="stat" style="left:653px">
    <svg class="badge" width="120" height="120" viewBox="0 0 120 120"><circle cx="60" cy="60" r="60" fill="#0d47a6"/><circle cx="60" cy="60" r="49" fill="none" stroke="#fff" stroke-width="3"/>
      <g transform="rotate(-35 60 60)"><path d="M44 50 L56 38 H78 V82 H56 L44 70 Z" fill="#fff"/><circle cx="52" cy="60" r="3" fill="#0d47a6"/>
      <text x="67" y="67" text-anchor="middle" font-family="Montserrat,sans-serif" font-weight="800" font-size="18" fill="#0d47a6">$</text></g></svg>
    <div class="figure">$500</div>
    <div class="fine"><b>/month</b> for our most affordable advertising package.</div>
  </section>

  <div class="cta">
    <p>Contact us today for targeted advertising on</p>
    <a href="#">www.tidecargomarket.com</a>
  </div>

  <footer class="footer">
    <div class="contact">
      <div class="org">Tide Cargo Market</div>
      <div class="row"><svg width="12" height="16" viewBox="0 0 12 16"><path d="M6 0a6 6 0 0 1 6 6c0 4-6 10-6 10S0 10 0 6a6 6 0 0 1 6-6z" fill="#0d4fb0"/><circle cx="6" cy="6" r="2.2" fill="#fff"/></svg><span>48 Harbourline Avenue #09-03<br>Singapore 049217</span></div>
      <div class="row gap"><svg width="14" height="14" viewBox="0 0 14 14"><path d="M3 0l3 3-2 2a8 8 0 0 0 5 5l2-2 3 3-2 3C6 14 0 8 0 2z" fill="#0d4fb0"/></svg><span>+65 6120 3374</span></div>
      <div class="row gap"><svg width="15" height="11" viewBox="0 0 15 11"><rect width="15" height="11" rx="1" fill="#0d4fb0"/><path d="M1 1l6.5 5L14 1" fill="none" stroke="#fff" stroke-width="1.3"/></svg><span>contact@tidecargomarket.com</span></div>
    </div>
    <div class="footer-brand">TideCargoMarket</div>
  </footer>
</main>
</body>
</html>
```